8" x 11" One Page Flyer for Fence Installation Company

We are looking to promote our business with a new flyer that would be handed out in person to people or put at their mailbox/door at their homes. The flyer needs to be creative and attention-grabbing. I have attached some of our previous flyers and our website information. Do not call or email regarding the flyer. We want the flyer to look professional but also friendly. One page, NOT folded. You can use images from our website at www.MyBraxtonYard.com or our Facebook page at www.Facebook.com/HollowbrookRailsBKT. We are flexible with what photos you can use but there must be photos of OUR fences on the flyer. More photos specifically can also be provided. Colors need to be suitable for a flyer printed on canary yellow in color paper OR white paper.

Target Market(s)

Homeowners that need a new fence

Industry/Entity Type

Construction

Font styles to use
Sans Serif
Other font styles liked:
• HD Colton

Colors
0054AA
0677BA
7BADD7
CADEEF
E8F1F8
0094D4
00A9DD
6FCCEA
C7EBF8
E9F6FB

Requirements
Must have
• Our fence photos - mostly wood fence photos (different designs), SIZE SHOULD BE LETTER SIZE 8" x 11"
Nice to have
• A nice bible verse featured at the bottom of the flyer.
Should not have
• DO NOT COPY THE WEBSITE FORMAT, I WANT SOMETHING UNIQUE. Other people's fence photos, they must all come from our website or facebook page

```html
<!DOCTYPE html>
<html lang="en">
<head>
<meta charset="utf-8">
<title>Hollowbrook Rails Flyer</title>
<link href="https://fonts.googleapis.com/css2?family=Montserrat:ital,wght@0,500;0,700;0,800;1,500&family=Poppins:wght@400;500;600&display=swap" rel="stylesheet">
<style>
  :root{
    --navy:#0054AA;
    --blue:#0677BA;
    --sky:#0094D4;
    --bright:#00A9DD;
    --pale:#E8F1F8;
    --ink:#111;
    --brown:#5a3a22;
    --bg:#e9ecef;
  }
  html,body{margin:0;padding:0;width:1200px;height:1200px;overflow:hidden;background:var(--bg);}
  .flyer{
    position:absolute;left:20px;top:152px;width:1752px;height:1352px;
    background:#fff;transform:scale(0.6621);transform-origin:0 0;
    font-family:'Poppins',sans-serif;color:var(--ink);
  }
  .abs{position:absolute;white-space:nowrap;}
  .brand-mark{left:70px;top:48px;width:120px;height:120px;background:var(--brown);}
  .brand-name{left:232px;top:42px;font-family:'Montserrat',sans-serif;font-weight:700;font-size:42px;color:var(--blue);}
  .brand-phone{left:232px;top:98px;font-family:'Montserrat',sans-serif;font-weight:800;font-size:56px;letter-spacing:1px;}
  .brand-tag{left:232px;top:176px;font-family:'Montserrat',sans-serif;font-weight:700;font-size:18px;}
  .hero{left:750px;top:12px;width:982px;height:196px;background:linear-gradient(180deg,var(--navy),var(--blue));color:#fff;overflow:hidden;}
  .hero h1{margin:0;position:absolute;left:32px;top:22px;font-family:'Montserrat',sans-serif;font-weight:800;font-size:72px;letter-spacing:-3px;white-space:nowrap;line-height:1.1;}
  .hero p{margin:0;position:absolute;left:32px;top:118px;font-family:'Poppins',sans-serif;font-size:40px;white-space:nowrap;line-height:1.2;}
  .photo{background:linear-gradient(160deg,#4f7d36 0%,#7ea04e 45%,#c9a86a 75%,#d8bf8a 100%);}
  .photo.iron{background:linear-gradient(160deg,#7fa458,#3f5f2c 60%,#2a2a2a);}
  .accent-square{left:301px;top:829px;width:132px;height:95px;background:var(--navy);}
  .why-head{left:1103px;top:238px;width:632px;height:88px;background:var(--sky);color:#fff;}
  .why-head h2{margin:0;position:absolute;left:20px;top:4px;font-family:'Montserrat',sans-serif;font-weight:800;font-size:40px;}
  .why-head p{margin:0;position:absolute;left:20px;top:54px;font-family:'Montserrat',sans-serif;font-weight:700;font-size:18px;}
  .perks{left:1118px;top:338px;margin:0;padding:0;list-style:none;}
  .perks li{display:flex;align-items:center;height:44.5px;font-size:32px;}
  .perks svg{width:24px;height:24px;margin-right:12px;flex:none;}
  .perks b{font-family:'Montserrat',sans-serif;font-weight:700;color:var(--navy);}
  .rule{left:1250px;top:724px;width:338px;height:3px;background:var(--navy);}
  .showroom{left:1103px;top:742px;width:632px;text-align:center;}
  .showroom h3{margin:0;font-family:'Montserrat',sans-serif;font-weight:800;font-size:28px;color:var(--navy);}
  .showroom p{margin:4px 0 0;font-size:24px;line-height:32px;}
  .hours{left:1105px;top:864px;width:613px;height:54px;border-radius:27px;background:var(--navy);color:#fff;font-family:'Montserrat',sans-serif;font-weight:800;font-size:25px;letter-spacing:-0.3px;line-height:54px;text-align:center;}
  .where{left:778px;top:947px;width:954px;height:286px;background:var(--sky);color:#fff;}
  .map{left:5px;top:3px;width:280px;height:280px;background:linear-gradient(135deg,#eef0f2,#dfe6e9 60%,#d6e4cf);}
  .where h2{margin:0;position:absolute;left:300px;top:8px;font-family:'Montserrat',sans-serif;font-weight:800;font-size:40px;}
  .where .addr{left:302px;top:74px;font-size:31px;}
  .where .phone{left:302px;top:128px;font-family:'Montserrat',sans-serif;font-weight:800;font-size:52px;display:flex;align-items:center;gap:8px;}
  .where .line{left:302px;display:flex;align-items:center;gap:14px;font-size:31px;}
  .where svg{flex:none;}
  .verse{left:20px;top:1250px;width:1713px;height:80px;background:linear-gradient(90deg,var(--navy),var(--blue));color:#fff;font-family:'Montserrat',sans-serif;font-style:italic;font-weight:500;font-size:42px;line-height:80px;text-align:center;}
</style>
</head>
<body>
<div class="flyer">
  <div class="abs brand-mark"></div>
  <div class="abs brand-name">Hollowbrook Rails</div>
  <div class="abs brand-phone">555-014-2236</div>
  <div class="abs brand-tag">“Because Good Fences Make Good Neighbors”</div>

  <div class="abs hero">
    <h1>WE BUILD FENCES....</h1>
    <p>And we would love to build your fence too!</p>
  </div>

  <div class="abs photo" style="left:20px;top:238px;width:408px;height:572px" role="img" aria-label="Split-rail wood fence with wire mesh and arched wooden gate beside a house"></div>
  <div class="abs photo" style="left:452px;top:238px;width:626px;height:454px" role="img" aria-label="Split-rail fence and arched wooden gate over a paver walkway"></div>
  <div class="abs photo iron" style="left:454px;top:714px;width:304px;height:212px" role="img" aria-label="Black metal picket fence around a backyard lawn"></div>
  <div class="abs photo" style="left:774px;top:714px;width:304px;height:212px" role="img" aria-label="Scalloped wooden privacy fence around a patio"></div>
  <div class="abs photo" style="left:20px;top:834px;width:264px;height:394px" role="img" aria-label="Tall wooden privacy fence along a planted garden bed"></div>
  <div class="abs accent-square"></div>
  <div class="abs photo" style="left:303px;top:948px;width:454px;height:282px" role="img" aria-label="Pointed wooden picket fence beside a house"></div>

  <div class="abs why-head">
    <h2>WHY CHOOSE US?</h2>
    <p>Beautiful, professionally installed fences at affordable prices!</p>
  </div>
  <ul class="abs perks">
    <li><svg viewBox="0 0 24 24"><circle cx="12" cy="12" r="10" fill="none" stroke="#0054AA" stroke-width="2"/><path d="M7 12.5l3.2 3L17 9" fill="none" stroke="#0054AA" stroke-width="2"/></svg>Free Estimates</li>
    <li><svg viewBox="0 0 24 24"><circle cx="12" cy="12" r="10" fill="none" stroke="#0054AA" stroke-width="2"/><path d="M7 12.5l3.2 3L17 9" fill="none" stroke="#0054AA" stroke-width="2"/></svg>Professional Installation</li>
    <li><svg viewBox="0 0 24 24"><circle cx="12" cy="12" r="10" fill="none" stroke="#0054AA" stroke-width="2"/><path d="M7 12.5l3.2 3L17 9" fill="none" stroke="#0054AA" stroke-width="2"/></svg>Concrete in&nbsp;<b>EVERY</b>&nbsp;Post</li>
    <li><svg viewBox="0 0 24 24"><circle cx="12" cy="12" r="10" fill="none" stroke="#0054AA" stroke-width="2"/><path d="M7 12.5l3.2 3L17 9" fill="none" stroke="#0054AA" stroke-width="2"/></svg>HOA Submission Assistance</li>
    <li><svg viewBox="0 0 24 24"><circle cx="12" cy="12" r="10" fill="none" stroke="#0054AA" stroke-width="2"/><path d="M7 12.5l3.2 3L17 9" fill="none" stroke="#0054AA" stroke-width="2"/></svg>Lifetime Workmanship Warranty</li>
    <li><svg viewBox="0 0 24 24"><circle cx="12" cy="12" r="10" fill="none" stroke="#0054AA" stroke-width="2"/><path d="M7 12.5l3.2 3L17 9" fill="none" stroke="#0054AA" stroke-width="2"/></svg>Experienced Installation Teams</li>
    <li><svg viewBox="0 0 24 24"><circle cx="12" cy="12" r="10" fill="none" stroke="#0054AA" stroke-width="2"/><path d="M7 12.5l3.2 3L17 9" fill="none" stroke="#0054AA" stroke-width="2"/></svg>Quality Workmanship &amp; Materials</li>
    <li><svg viewBox="0 0 24 24"><circle cx="12" cy="12" r="10" fill="none" stroke="#0054AA" stroke-width="2"/><path d="M7 12.5l3.2 3L17 9" fill="none" stroke="#0054AA" stroke-width="2"/></svg><b>FREE</b>&nbsp;Gate Adjustments for&nbsp;<b>LIFE</b></li>
  </ul>

  <div class="abs rule"></div>
  <div class="abs showroom">
    <h3>Visit our indoor &amp; outdoor showroom!</h3>
    <p>Our outdoor showroom is open 24/7, while our<br>indoor showroom and office is open Monday</p>
  </div>
  <div class="abs hours">THURS 9AM - 3PM, FRIDAY 9AM - 1PM</div>

  <div class="abs where">
    <div class="abs map" role="img" aria-label="Street map showing the office location"></div>
    <h2>WHERE ARE WE?</h2>
    <div class="abs addr">418 Millpond Rd Braxton, NC 28990</div>
    <div class="abs phone"><svg width="40" height="40" viewBox="0 0 24 24"><path d="M6.6 10.8a15 15 0 006.6 6.6l2.2-2.2c.3-.3.7-.4 1-.2 1.1.4 2.300.6 3.6.6.6 0 1 .4 1 1V20c0 .6-.4 1-1 1A17 17 0 013 4c0-.6.4-1 1-1h3.5c.6 0 1 .4 1 1 0 1.3.2 2.5.6 3.6.1.3 0 .7-.2 1z" fill="#fff"/></svg>555-014-2236</div>
    <div class="abs line" style="top:184px"><svg width="26" height="26" viewBox="0 0 24 24"><rect x="2" y="5" width="20" height="14" fill="none" stroke="#fff" stroke-width="2"/><path d="M2 5l10 8 10-8" fill="none" stroke="#fff" stroke-width="2"/></svg>office@mybraxtonyard.com</div>
    <div class="abs line" style="top:226px"><svg width="26" height="26" viewBox="0 0 24 24"><circle cx="12" cy="12" r="10" fill="none" stroke="#fff" stroke-width="1.6"/><ellipse cx="12" cy="12" rx="4.5" ry="10" fill="none" stroke="#fff" stroke-width="1.6"/><path d="M2 12h20M4 7h16M4 17h16" stroke="#fff" stroke-width="1.4"/></svg><span>www.<b style="font-weight:600">MyBraxtonYard</b>.com</span></div>
  </div>

  <div class="abs verse">“Pursue the Lord and his strength; seek his face always!” — 1 Chronicles 16:11</div>
</div>
</body>
</html>
```